Pet sitting Business needs a website

We need a website that shows our services and prices. Shows our love of animals but also our professionalism. want a gallery, about, blog, services, links to fb and instagram accounts, newsletter archive. want it to be easy to access and wonderful to navigate. want the domain to be Brindlecovepawhouse.com
take any info from FB site www.facebook.com/brindlecovepawhouse
I would like it to fit square space platform

Target Market(s)

upscale area, responsible pet owners,

Industry/Entity Type

Pet Care

Coding

Coded - Design and coding required

Number of Pages Required

5+ page

Font styles to use
Sans Serif

Requirements
Must have
• (square space platform)
• Menu
• photo gallery
• about us
• services
• policies
• monthly newsletter
• unavailable dates
• Introduction (welcome)
• payment methods
• Daily updates
• testimonials (use from fb site)
Should not have
• stock photos

```html
<!DOCTYPE html>
<html lang="en">
<head>
<meta charset="utf-8">
<title>Brindle Cove Paw House</title>
<link href="https://fonts.googleapis.com/css2?family=Roboto:ital,wght@0,300;0,400;0,500;0,700;1,300&family=Reenie+Beanie&display=swap" rel="stylesheet">
<style>
:root{
  --blue:#1a8ccc;
  --blue-deep:#147ab8;
  --blue-light:#3fb6ef;
  --footer:#1a7fb5;
  --gold:#d9a82a;
  --badge:#d8a51c;
  --ink:#222;
  --body:#555;
  --muted:#777;
  --white:#fff;
  --dot:#c9a85a;
}
*{box-sizing:border-box;margin:0;padding:0}
html,body{width:1200px;height:2550px;overflow:hidden}
body{position:relative;font-family:'Roboto',sans-serif;color:var(--ink);background:var(--white)}
.abs{position:absolute}

/* top bar */
.topbar{left:0;top:0;width:1200px;height:34px;background:var(--white);display:flex;justify-content:flex-end;align-items:center;gap:26px;padding-right:52px;font-size:14px;color:var(--muted);font-weight:300}
.topbar span{display:flex;align-items:center;gap:6px}
.reserve{background:var(--badge);color:var(--white);font-weight:500;padding:3px 8px;border-radius:3px;font-size:14px}
.social-dot{width:12px;height:12px;border-radius:50%;background:#999;display:inline-block}

/* nav */
.navband{left:0;top:34px;width:1200px;height:71px;background:var(--blue-deep)}
.brand{left:54px;top:34px;width:283px;height:82px;background:var(--white);border-radius:0 0 8px 8px;box-shadow:0 2px 4px rgba(0,0,0,.15);display:flex;align-items:center;justify-content:center;gap:10px}
.brand-mark{width:22px;height:22px;border-radius:50%;background:var(--gold)}
.brand-name{font-size:24px;font-weight:500;color:var(--gold)}
.nav{right:52px;top:34px;height:71px;display:flex;align-items:center;gap:36px;list-style:none}
.nav li{color:var(--white);font-size:16px;font-weight:500;text-transform:uppercase}

/* hero */
.hero{left:0;top:105px;width:1200px;height:488px;background:radial-gradient(ellipse at 30% 55%,#c79552 0%,#8e6233 28%,#3e4a24 55%,#1f2a14 80%,#151a10 100%)}
.hero-title{left:728px;top:188px;width:460px;font-family:'Reenie Beanie',cursive;font-size:66px;line-height:54px;color:var(--white)}
.btn-light{background:var(--white);color:var(--blue);font-size:11px;font-weight:700;text-transform:uppercase;padding:0;height:32px;display:flex;align-items:center;justify-content:center;border-radius:2px}
.dots{left:568px;top:558px;display:flex;gap:9px}
.dots i{width:9px;height:9px;border-radius:50%;background:var(--white);display:block}
.dots i.open{background:transparent;border:1px solid var(--white)}

/* stats */
.stats{left:0;top:593px;width:1200px;height:240px;background:linear-gradient(180deg,#1d8fd4,#2aa3e3);display:flex;color:var(--white)}
.stat{flex:1;text-align:center;padding-top:22px}
.stat h3{font-size:20px;font-weight:300}
.stat .num{font-size:44px;font-weight:700;margin:12px 0 18px}
.stat p{font-size:13px;font-weight:300;line-height:19px;width:390px;margin:0 auto}

/* section headings */
.sec-title{width:1200px;left:0;text-align:center;font-size:22px;font-weight:700;color:var(--ink)}
.rule{left:55px;width:1094px;border-top:1px dashed var(--dot)}
.rule.light{border-top-color:rgba(255,255,255,.7)}

.about p{left:55px;width:1094px;text-align:center;font-size:13px;line-height:20px;color:var(--muted);font-weight:300}

/* services */
.services{left:0;top:1105px;width:1200px;height:326px;background:radial-gradient(ellipse at 60% 100%,var(--blue-light) 0%,#2299dc 45%,var(--blue-deep) 100%)}
.service-row{left:55px;top:1220px;width:1110px;display:flex}
.service{flex:1;display:flex;flex-direction:column;align-items:center;border-right:1px dashed rgba(255,255,255,.6);height:110px}
.service:last-child{border-right:none}
.service svg{height:76px}
.service span{color:var(--white);font-size:18px;font-weight:700;margin-top:8px}

/* gallery */
.gallery{left:0;top:1525px;width:1200px;height:180px;display:flex}
.gallery div{flex:1;height:180px}

/* testimonials */
.quote{font-size:13px;font-style:italic;font-weight:300;line-height:19px;color:var(--body);width:400px}
.quote b{display:block;font-style:normal;font-weight:500;color:var(--ink);margin-top:6px}
.quote.left{text-align:right}
.avatar{width:78px;height:78px;border-radius:50%;background:#b5b5b5;display:flex;align-items:center;justify-content:center;font-size:10px;color:#333}
.vdivider{left:600px;top:1815px;height:250px;border-left:1px dashed #ddd}
.hdivider{left:55px;top:1930px;width:1094px;border-top:1px dashed #eee}

/* footer */
.footer{left:0;top:2111px;width:1200px;height:439px;background:var(--footer);color:var(--white)}
.fcol{top:2160px;width:260px}
.fcol h4{font-size:18px;font-weight:500;margin-bottom:16px}
.fcol p{font-size:13px;line-height:20px;font-weight:300;margin-bottom:14px}
.fcol strong{font-weight:700}
.field{width:254px;height:32px;background:var(--white);border-radius:3px;margin-bottom:10px;font-size:12px;color:#999;padding:9px 12px}
.field.area{height:52px}
.send{width:135px;height:32px;background:var(--white);color:var(--ink);font-size:13px;font-weight:500;text-transform:uppercase;display:flex;align-items:center;justify-content:center;border-radius:3px}
.fsocial{display:flex;gap:12px;margin-top:4px}
.fsocial i{width:11px;height:11px;border-radius:50%;background:var(--white);display:block}
.map{width:254px;height:210px;background:linear-gradient(135deg,#c9dbe8,#a9c7dd 55%,#e3e6d9)}
.frule{left:53px;top:2479px;width:1096px;border-top:1px solid rgba(255,255,255,.35)}
.copyright{left:0;top:2505px;width:1200px;text-align:center;font-size:13px;font-weight:500}
</style>
</head>
<body>

<div class="abs topbar">
  <span><svg width="12" height="12" viewBox="0 0 24 24"><path fill="#999" d="M6.6 10.8a15 15 0 006.6 6.6l2.2-2.2a1 1 0 011-.25 11.4 11.4 0 003.6.57 1 1 0 011 1V20a1 1 0 01-1 1A17 17 0 013 4a1 1 0 011-1h3.5a1 1 0 011 1 11.4 11.4 0 00.57 3.6 1 1 0 01-.25 1z"/></svg>210-555-0148</span>
  <span><svg width="13" height="10" viewBox="0 0 26 20"><rect width="26" height="20" rx="2" fill="#999"/><path d="M1 2l12 9 12-9" stroke="#fff" stroke-width="2" fill="none"/></svg>brindlecovepawhouse@gmail.com</span>
  <span class="reserve">Online Reservations</span>
  <span><i class="social-dot"></i><i class="social-dot" style="margin-left:14px"></i></span>
</div>

<div class="abs navband"></div>
<div class="abs brand"><span class="brand-mark"></span><span class="brand-name">Brindle Cove Paw House</span></div>
<ul class="abs nav">
  <li>Hi !</li><li>About Us</li><li>Services</li><li>Gallery</li><li>Blog</li><li>Policies</li><li>Contact</li>
</ul>

<div class="abs hero" role="img" aria-label="Close-up photo of a golden retriever on a grassy lawn"></div>
<div class="abs hero-title">Where Kisses and Hugs are my Speciality</div>
<div class="abs btn-light" style="left:734px;top:389px;width:100px">Our Services</div>
<div class="abs btn-light" style="left:870px;top:389px;width:106px">Go on Surfing</div>
<div class="abs dots"><i class="open"></i><i></i><i></i><i></i></div>

<section class="abs stats">
  <div class="stat"><h3>Dog park in 2016</h3><div class="num">87000 +</div><p>I was a Licensed Veterinarian Technician Supervisor of a major animal hospital in Nashville.</p></div>
  <div class="stat"><h3>Satisfied Clients</h3><div class="num">100 +</div><p>Given their satisfaction with our work, the majority of the clients have become our partners they turn to us as year after year with their research problems</p></div>
  <div class="stat"><h3>Experience</h3><div class="num">20 +</div><p>I have spent 20 years of my life taking care of our friends and would to do the same for yours.</p></div>
</section>

<section class="about">
  <h2 class="abs sec-title" style="top:866px">Hi my name is Marla Desoto</h2>
  <div class="abs rule" style="top:908px"></div>
  <p class="abs" style="top:960px">Hi my name is Marla Desoto and I would love to introduce myself. I am a Licensed Veterinarian Technician from Nashville, Tennessee. My family and I moved to San Antonio in 2008. I have dedicated the last 13 years to raising my 2 beautiful children and 5 of my furry babies.</p>
  <p class="abs" style="top:1020px">I have the knowledge and the training to give the special care your pet will need. I was a Licensed Veterinarian Technician Supervisor of a major animal hospital in Nashville. I have spent 20 years of my life taking care of our friends and would to do the same for yours</p>
</section>

<section class="abs services"></section>
<h2 class="abs sec-title" style="top:1145px;color:var(--white)">Our Services</h2>
<div class="abs rule light" style="top:1185px"></div>
<div class="abs service-row">
  <div class="service">
    <svg viewBox="0 0 80 76" width="80"><path fill="#fff" d="M22 10a12 12 0 0112 12c0 10-12 24-12 24S10 32 10 22a12 12 0 0112-12z"/><path fill="#e6f4fc" d="M58 16a11 11 0 0111 11c0 9-11 22-11 22S47 36 47 27a11 11 0 0111-11z"/><path fill="#fff" d="M40 22a14 14 0 0114 14c0 12-14 28-14 28S26 48 26 36a14 14 0 0114-14z"/><circle cx="40" cy="36" r="5" fill="#2a9ddd"/><ellipse cx="40" cy="70" rx="26" ry="4" fill="#fff" opacity=".7"/></svg>
    <span>Daily Visit</span>
  </div>
  <div class="service">
    <svg viewBox="0 0 80 76" width="80" fill="#fff"><g transform="translate(4 6)"><ellipse cx="10" cy="12" rx="7" ry="5"/><circle cx="3" cy="5" r="2.5"/><circle cx="9" cy="2" r="2.5"/><circle cx="16" cy="4" r="2.5"/></g><g transform="translate(46 14)"><ellipse cx="10" cy="12" rx="7" ry="5"/><circle cx="3" cy="5" r="2.5"/><circle cx="9" cy="2" r="2.5"/><circle cx="16" cy="4" r="2.5"/></g><g transform="translate(10 36)"><ellipse cx="10" cy="12" rx="7" ry="5"/><circle cx="3" cy="5" r="2.5"/><circle cx="9" cy="2" r="2.5"/><circle cx="16" cy="4" r="2.5"/></g><g transform="translate(50 48)"><ellipse cx="10" cy="12" rx="7" ry="5"/><circle cx="3" cy="5" r="2.5"/><circle cx="9" cy="2" r="2.5"/><circle cx="16" cy="4" r="2.5"/></g></svg>
    <span>Just walks</span>
  </div>
  <div class="service">
    <svg viewBox="0 0 80 76" width="80" fill="#fff"><ellipse cx="40" cy="64" rx="32" ry="10"/><ellipse cx="40" cy="48" rx="24" ry="10"/><ellipse cx="40" cy="33" rx="16" ry="8"/><path d="M34 26c2-8 8-14 14-20-1 8 0 14-6 20z"/></svg>
    <span>Potty visits</span>
  </div>
  <div class="service">
    <svg viewBox="0 0 80 76" width="80" fill="#fff"><circle cx="40" cy="24" r="18"/><rect x="37" y="38" width="6" height="30"/><rect x="10" y="68" width="60" height="4" rx="2"/><rect x="52" y="52" width="22" height="4" rx="1"/><rect x="54" y="56" width="3" height="12"/><rect x="69" y="56" width="3" height="12"/></svg>
    <span>Dog park</span>
  </div>
  <div class="service">
    <svg viewBox="0 0 80 76" width="80"><rect x="24" y="2" width="32" height="10" rx="2" fill="#fff"/><rect x="20" y="14" width="40" height="60" rx="6" fill="none" stroke="#fff" stroke-width="4"/><circle cx="40" cy="46" r="14" fill="none" stroke="#fff" stroke-width="3"/><g fill="#fff"><ellipse cx="40" cy="50" rx="5" ry="4"/><circle cx="34" cy="43" r="2"/><circle cx="39" cy="40" r="2"/><circle cx="45" cy="42" r="2"/></g></svg>
    <span>Medication</span>
  </div>
</div>

<h2 class="abs sec-title" style="top:1452px">Photo Gallery</h2>
<div class="abs rule" style="top:1493px"></div>
<div class="abs gallery">
  <div role="img" aria-label="Photo of a cat held close by its owner" style="background:linear-gradient(135deg,#4a3a2e,#8c6a52 60%,#2a2420)"></div>
  <div role="img" aria-label="Photo of a curly brown dog resting on a bed" style="background:linear-gradient(135deg,#6d5a3e,#b07a4c 45%,#e8e4de)"></div>
  <div role="img" aria-label="Photo of a black and white cat" style="background:linear-gradient(135deg,#3d4a3a,#1c1f1b 50%,#dcdcd6)"></div>
  <div role="img" aria-label="Photo of two fluffy puppies on a patio" style="background:linear-gradient(180deg,#8a8f86,#b08660 55%,#cfc8bc)"></div>
  <div role="img" aria-label="Photo of a shaggy dog beside a child" style="background:linear-gradient(135deg,#3a2a20,#a8744a 45%,#c24040)"></div>
</div>

<h2 class="abs sec-title" style="top:1722px">What People Say</h2>
<div class="abs rule" style="top:1761px"></div>
<div class="abs vdivider"></div>
<div class="abs hdivider"></div>

<div class="abs quote left" style="left:62px;top:1818px">Duis aute irure dolor in reprehenderit in voluptate velit esse cillum dolore eu fugiat nulla pariatur. Excepteur sint occaecat cupidatat non proident, sunt in culpa qui officia deserunt mollit.<b>Evan Pruitt, Operations Manager</b></div>
<div class="abs avatar" style="left:490px;top:1820px">170x170</div>
<div class="abs avatar" style="left:632px;top:1820px">170x170</div>
<div class="abs quote" style="left:738px;top:1818px">Provident, similique sunt in culpa qui officia deserunt mollitia animi, id est laborum et dolorum fuga. Et harum quidem rerum facilis est et expedita distinctio. Nam libero tempore, cum soluta nobis.<b>Nora Vance, Creative Designer</b></div>

<div class="abs quote left" style="left:62px;top:1955px">Luis aute irure dolor in reprehenderit in piluptate velit esse cillum dolore eu fugiat nulla pariatur. Excepteur sint occaecat cupidatat non proident, sunt in culpa qui officia deserunt mollit.<b>Greta Holm, Manager</b></div>
<div class="abs avatar" style="left:490px;top:1956px">170x170</div>
<div class="abs avatar" style="left:632px;top:1956px">170x170</div>
<div class="abs quote" style="left:738px;top:1955px">At vero eos et accusamus et iusto odio dignissimos ducimus qui blanditiis praesentium voluptatum deleniti atque corrupti quos dolores et quas molestias excepturi sint occaecati asperiores.<b>Owen Marsh, Developer</b></div>

<footer class="abs footer"></footer>
<div class="abs fcol" style="left:53px;color:var(--white)">
  <h4>Contact Us</h4>
  <p>Maecenas etos sit amet, consectetur adipiscing elit. Terminal volutpat rutrum metro amet sollicitudin interdum.</p>
  <p><strong>Phone:</strong> +1 (800) 555 01 96</p>
  <p><strong>Office:</strong> 4410 Larkin Street, New York</p>
  <p><strong>Email:</strong> info@brindlecovepaw.com</p>
  <div class="fsocial"><i></i><i></i><i></i><i></i><i></i></div>
</div>
<div class="abs fcol" style="left:333px;color:var(--white)">
  <h4>Feel Free to Mail</h4>
  <div class="field">Name *</div>
  <div class="field">Email *</div>
  <div class="field area">Write Your Message Here...</div>
  <div class="send">Send Message</div>
</div>
<div class="abs fcol" style="left:614px;color:var(--white)">
  <h4>Area Map</h4>
  <div class="map" role="img" aria-label="Street map of the business location"></div>
</div>
<div class="abs fcol" style="left:896px;color:var(--white);width:256px">
  <h4>About Team</h4>
  <p>Enim congue blandit. Lorem ipsum dolor sit amet, consectetur adipiscing elit. Quisque consectetur interdum finibus. Vestibulum ante ipsum primis in faucibus orci. luctus et ultrices posuere.</p>
  <p>Cubilia cras blandit finibus ipsum, id porttitor arcu volutpat a. Integer iaculis erat nec justo malesuada faucibus vel tempus sapien. Vivamus aliquam euismod tristique.</p>
</div>
<div class="abs frule"></div>
<div class="abs copyright" style="color:var(--white)">Copyright 2020. All Rights Reserved</div>

</body>
</html>
```